3D Printing Business coming soon page

Hi we are looking for a one page "coming soon" website for our business. The business is called "Solevia Labs" and it is a new solution which 3D Prints Orthotics (Insoles).

The design should include our logo, an improved version of our promotional image (attached), a web form for capturing interest from people, a countdown timer and some text.

Follow the colour scheme which is shown in our logo along with our other colours - Orange (RGB#ff8300) and Light Green (RGB#30f20a)
Updates

Industry/Entity Type

Business

Font styles to use
Sans Serif

Requirements
Must have
• Logo (Attached)
Improved version of Promotional Image
Web Form design for capturing Name, EMail Address and Comments along with a Turin test
Countdown Timer
Text - "Solevia Labs will shake up the Orthotics Industry. Foot Orthosis patient-ready in hours for a fraction of the price you are paying today. Welcome to the new world of 3D Printing!"

```html
<!DOCTYPE html>
<html lang="en">
<head>
<meta charset="utf-8">
<title>Solevia Labs — Coming Soon</title>
<link rel="stylesheet" href="https://fonts.googleapis.com/css2?family=Open+Sans:wght@300;400;600;700&display=swap">
<style>
  :root {
    --navy: #2c2b5e;
    --sky-top: #aee0f1;
    --sky-bottom: #8fd2ea;
    --green: #7dbd22;
    --ring: #cdeaf5;
    --orange: #e2812f;
    --white: #ffffff;
    --placeholder: #9a98b8;
  }
  * { box-sizing: border-box; margin: 0; padding: 0; }
  html, body { width: 1200px; height: 1050px; overflow: hidden; }
  body {
    position: relative;
    font-family: "Open Sans", Arial, sans-serif;
    color: var(--navy);
    background: linear-gradient(180deg, var(--sky-top) 0%, var(--sky-bottom) 40%, var(--sky-bottom) 100%);
  }
  .top-bar, .site-footer {
    position: absolute; left: 0; width: 1200px; height: 60px;
    background: var(--navy); color: var(--white);
    font-family: Arial, Helvetica, sans-serif; font-size: 12px;
  }
  .top-bar { top: 0; }
  .top-bar .tagline { position: absolute; right: 226px; top: 24px; color: #dcdcec; }
  .top-bar .tagline strong { color: var(--white); }
  .social { position: absolute; right: 111px; top: 15px; display: flex; gap: 6px; }
  .social a {
    display: flex; align-items: center; gap: 4px;
    color: var(--white); text-decoration: none; font-size: 10px; line-height: 30px;
  }
  .social .dot { width: 10px; height: 10px; background: #2fb5ea; }
  .site-footer { top: 990px; }
  .site-footer p { position: absolute; left: 111px; top: 24px; color: #dcdcec; }
  .site-footer strong { color: var(--white); }

  .brand {
    position: absolute; left: 200px; top: 180px; width: 296px;
    display: flex; align-items: center; justify-content: center; gap: 12px;
    font-size: 42px; font-weight: 700; color: var(--navy); letter-spacing: -0.5px;
  }
  .brand .mark { width: 22px; height: 22px; border-radius: 50%; background: #1a8fc9; }

  .headline {
    position: absolute; left: 111px; top: 318px;
    font-size: 34px; font-weight: 300; line-height: 42px;
  }
  .headline strong { font-weight: 600; }
  .intro {
    position: absolute; left: 111px; top: 418px; width: 490px;
    font-size: 18px; font-weight: 400; line-height: 28px;
  }

  .signup-form .field {
    position: absolute; left: 111px; width: 474px; height: 50px;
    border: none; border-radius: 4px; background: var(--white);
    font: 300 18px "Open Sans", sans-serif; color: var(--navy);
    padding: 12px 19px;
  }
  .signup-form .field::placeholder { color: var(--placeholder); }
  .field.name { top: 543px; }
  .field.email { top: 603px; }
  .field.message { top: 663px; height: 116px; resize: none; }
  .captcha-label { position: absolute; left: 111px; top: 800px; font-size: 18px; }
  .field.captcha { top: 789px; left: 417px !important; width: 168px !important; }
  .send-button {
    position: absolute; left: 111px; top: 859px; width: 222px; height: 50px;
    border: none; border-radius: 4px; background: var(--orange); color: var(--white);
    font: 700 18px "Open Sans", sans-serif; text-transform: uppercase;
  }

  .steps { position: absolute; left: 712px; top: 136px; width: 280px; list-style: none; }
  .step { height: 187px; text-align: center; }
  .step h2 { font-size: 24px; font-weight: 600; line-height: 32px; }
  .step .badge {
    width: 132px; height: 132px; margin: 2px auto 0; border-radius: 50%;
    background: var(--ring); display: flex; align-items: center; justify-content: center;
  }
  .step .badge span {
    width: 116px; height: 116px; border-radius: 50%; background: var(--green);
    display: flex; align-items: center; justify-content: center;
  }
</style>
</head>
<body>
  <header class="top-bar">
    <p class="tagline">Lorem ipsum dolor sit amet sed do eiusmod tempor <strong>incididunt ut labore</strong> et dolore magna aliqua.</p>
    <nav class="social">
      <a href="#"><span class="dot"></span>Facetome</a>
      <a href="#"><span class="dot"></span>Chirper</a>
    </nav>
  </header>

  <div class="brand"><span class="mark"></span>Solevia Labs</div>

  <h1 class="headline"><strong>Solevia Labs</strong> will shake up the<br><strong>Orthotics Industry.</strong></h1>
  <p class="intro">Foot Orthosis patient-ready in hours for a fraction of the price you are paying today. Welcome to the new world of 3D Printing!</p>

  <form class="signup-form">
    <input class="field name" type="text" placeholder="Type your Name">
    <input class="field email" type="email" placeholder="Type your E-mail Address">
    <textarea class="field message" placeholder="Message"></textarea>
    <label class="captcha-label" for="captcha">Are you human? What is 16 + 4 =</label>
    <input class="field captcha" id="captcha" type="text">
    <button class="send-button" type="submit">Send Message</button>
  </form>

  <ol class="steps">
    <li class="step">
      <h2>Scan the foot</h2>
      <div class="badge"><span>
        <svg width="66" height="66" viewBox="0 0 66 66" fill="none" stroke="#fff" stroke-width="4" stroke-linejoin="round">
          <path d="M6 40 L38 24 L60 36 L28 54 Z" fill="#fff"/>
          <path d="M14 40 L36 29 L50 37 L28 48 Z" fill="#7dbd22" stroke="none"/>
          <path d="M38 24 L30 10 L50 22"/>
          <path d="M20 38 L34 46" stroke="#fff" stroke-width="3"/>
        </svg>
      </span></div>
    </li>
    <li class="step">
      <h2>Design the Orthotic</h2>
      <div class="badge"><span>
        <svg width="60" height="66" viewBox="0 0 60 66" fill="none" stroke="#fff" stroke-width="3" stroke-linejoin="round">
          <path d="M8 18 L16 6 L24 18 V58 H8 Z"/>
          <path d="M8 18 H24 M14 24 V52 M18 24 V52"/>
          <rect x="32" y="4" width="18" height="58"/>
          <path d="M32 12 H40 M32 20 H38 M32 28 H40 M32 36 H38 M32 44 H40 M32 52 H38"/>
        </svg>
      </span></div>
    </li>
    <li class="step">
      <h2>3D Print it</h2>
      <div class="badge"><span>
        <svg width="60" height="60" viewBox="0 0 60 60" fill="#fff">
          <rect x="14" y="4" width="32" height="24" rx="3"/>
          <rect x="20" y="10" width="20" height="12" fill="#7dbd22"/>
          <rect x="4" y="24" width="52" height="32" rx="4"/>
          <rect x="12" y="42" width="36" height="4" fill="#7dbd22"/>
          <circle cx="14" cy="33" r="2.5" fill="#7dbd22"/>
        </svg>
      </span></div>
    </li>
    <li class="step">
      <h2>Fit it</h2>
      <div class="badge"><span>
        <svg width="40" height="66" viewBox="0 0 40 66" fill="#fff">
          <path d="M20 2 C32 2 34 14 32 26 C30 36 26 40 12 40 C8 30 6 20 8 12 C10 5 14 2 20 2 Z"/>
          <path d="M11 46 H28 L26 60 C25 64 14 64 13 60 Z"/>
        </svg>
      </span></div>
    </li>
  </ol>

  <footer class="site-footer">
    <p>© 2014 <strong>Solevia Labs</strong>. All rights reserved.</p>
  </footer>
</body>
</html>
```